Silver Falcon Construction Services

Create a business card for my business consulting company
Marissa Vendt, Founder and CEO
4816 Willow Crest Ave, Ste 210
Larkspur Ridge, CO. 80599
720.555.0187 cell
mvendt@silverfalconbuild.example
www.silverfalconbuild.example

Target Market(s)

Private Equity and Construction Companies

Industry/Entity Type

Business / Sales Consulting

Tag Line that says "Where The Road To Success Is Always Under Construction"

Requirements
Must have
• Logo on both sides of the card.
Nice to have
• Add tagline to the same side of the card as my name and contact info

```html
<!DOCTYPE html>
<html lang="en">
<head>
<meta charset="utf-8">
<title>Silver Falcon Construction Services – Business Card</title>
<link href="https://fonts.googleapis.com/css2?family=Roboto:wght@400;500;700&display=swap" rel="stylesheet">
<style>
  :root {
    --backdrop: #e6ddd1;
    --card-clear: rgba(250, 246, 240, 0.55);
    --card-edge: rgba(255, 255, 255, 0.85);
    --panel-black: #111010;
    --accent-sand: #d9c7a9;
    --ink-dark: #2b2824;
  }
  * { box-sizing: border-box; margin: 0; padding: 0; }
  html, body {
    width: 1200px; height: 1046px; overflow: hidden;
    background: var(--backdrop);
    font-family: "Roboto", Arial, sans-serif;
  }
  .card {
    position: absolute; left: 151px; top: 292px;
    width: 946px; height: 514px;
    border-radius: 28px;
    background: var(--card-clear);
    border: 1.5px solid var(--card-edge);
    box-shadow: 0 18px 40px rgba(60, 45, 30, 0.18);
    overflow: hidden;
  }
  .card__panel {
    position: absolute; inset: 0;
    background: var(--panel-black);
    clip-path: polygon(372px 0, 100% 0, 100% 100%, 340px 100%, 672px 195px);
  }
  .tagline {
    position: absolute; left: 187px; top: 228px; width: 300px;
    text-align: center; color: var(--ink-dark);
    font-size: 19px; line-height: 28px; letter-spacing: 0.2px;
  }
  .brand {
    position: absolute; right: 38px; top: 40px; width: 260px;
    text-align: center; color: var(--accent-sand);
    font-weight: 500; text-transform: uppercase;
  }
  .brand__mark {
    width: 40px; height: 40px; border-radius: 50%;
    background: var(--accent-sand); margin: 0 auto 14px;
  }
  .brand__name { font-size: 24px; letter-spacing: 1px; line-height: 28px; }
  .brand__sub { font-size: 10.5px; letter-spacing: 2.4px; margin-top: 4px; }
  .contact {
    position: absolute; right: 38px; top: 242px;
    text-align right; text-align: right; color: var(--accent-sand);
  }
  .contact__name { font-size: 34px; line-height: 40px; font-weight: 400; }
  .contact__name strong { font-weight: 700; }
  .contact__role { font-size: 19px; margin-top: 2px; }
  .contact__address { font-size: 19px; line-height: 28px; margin-top: 30px; }
  .contact__lines { list-style: none; margin-top: 18px; font-size: 19px; line-height: 28px; }
  .contact__lines li { display: flex; justify-content: flex-end; align-items: center; gap: 14px; }
  .contact__lines svg { width: 18px; height: 18px; fill: none; stroke: var(--accent-sand); stroke-width: 1.8; }
  .edge-tab {
    position: absolute; right: 0; top: 242px; width: 17px; height: 61px;
    background: var(--accent-sand);
  }
</style>
</head>
<body>
  <div class="card">
    <div class="card__panel"></div>
    <p class="tagline">The Road To Success Is<br>Always Under Construction</p>

    <div class="brand">
      <div class="brand__mark"></div>
      <div class="brand__name">Silver Falcon</div>
      <div class="brand__sub">Construction Services</div>
    </div>

    <div class="contact">
      <h1 class="contact__name"><strong>Marissa</strong> Vendt</h1>
      <p class="contact__role">Founder and CEO</p>
      <p class="contact__address">4816 Willow Crest Ave, Ste 210<br>Larkspur Ridge, CO. 80599</p>
      <ul class="contact__lines">
        <li>720.555.0187
          <svg viewBox="0 0 24 24"><path d="M5 3h4l2 5-2.5 1.5a11 11 0 0 0 6 6L16 13l5 2v4a2 2 0 0 1-2 2A16 16 0 0 1 3 5a2 2 0 0 1 2-2z"/></svg>
        </li>
        <li>www.silverfalconbuild.example
          <svg viewBox="0 0 24 24"><circle cx="12" cy="12" r="9"/><path d="M3 12h18M12 3c3 3 3 15 0 18M12 3c-3 3-3 15 0 18"/></svg>
        </li>
        <li>mvendt@silverfalconbuild.example
          <svg viewBox="0 0 24 24"><rect x="3" y="6" width="18" height="13" rx="1"/><path d="M3 7l9 7 9-7"/></svg>
        </li>
      </ul>
    </div>
    <div class="edge-tab"></div>
  </div>
</body>
</html>
```